Korvo Suplies

Packaging design for Multitool Blades, something similar to the drawing on paper, diecut of the packaging attached

Logo Text

Korvo Supplies

```html
<!DOCTYPE html>
<html lang="en">
<head>
<meta charset="utf-8">
<title>Korvo Supplies – Multitool Blade Packaging</title>
<link href="https://fonts.googleapis.com/css2?family=Roboto:wght@700&display=swap" rel="stylesheet">
<style>
  :root {
    --brand-green: #32b356;
    --backdrop-blue: #0277bf;
    --card-black: #000000;
    --paper-white: #ffffff;
    --window-outline: #f8fafc;
    --label-dark: #2b2b2b;
    --timber-light: #d9bd95;
    --timber-mid: #c49a6c;
    --hardwood: #6b4a2e;
    --plywood-top: #6f8796;
  }
  html, body {
    margin: 0;
    padding: 0;
    width: 1200px;
    height: 1200px;
    overflow: hidden;
    background: var(--paper-white);
  }
  .canvas { display: block; width: 1200px; height: 1200px; }
  .backdrop-light { fill: var(--paper-white); }
  .backdrop-blue { fill: var(--backdrop-blue); }
  .card-body { fill: var(--card-black); }
  .hang-tab, .accent-sweep { fill: var(--brand-green); }
  .brand-square { fill: var(--brand-green); }
  .brand-name {
    font-family: "Roboto", sans-serif;
    font-weight: 700;
    font-size: 44px;
    fill: var(--paper-white);
  }
  .product-window {
    fill: var(--brand-green);
    stroke: var(--window-outline);
    stroke-width: 22;
    stroke-linejoin: round;
  }
  .material-tile { fill: var(--paper-white); }
  .material-band { fill: var(--label-dark); }
  .material-label {
    font-family: "Roboto", sans-serif;
    font-weight: 700;
    font-size: 10px;
    fill: var(--paper-white);
  }
</style>
</head>
<body>
<svg class="canvas" viewBox="0 0 1500 1500" xmlns="http://www.w3.org/2000/svg">
  <defs>
    <linearGradient id="timberTone" x1="0" y1="0" x2="1" y2="1">
      <stop offset="0" stop-color="var(--timber-light)"/>
      <stop offset="1" stop-color="var(--timber-mid)"/>
    </linearGradient>

    <g id="blade-pack">
      <rect class="card-body" x="120" y="196" width="516" height="1108"/>

      <path class="timber-photo" role="img" aria-label="Photo of stacked timber planks"
            fill="url(#timberTone)"
            d="M120 196 Q285 285 346 449 L120 449 Z"/>

      <g class="hang-tab">
        <rect x="284" y="248" width="203" height="41" rx="20.5"/>
        <circle cx="385" cy="248" r="27"/>
      </g>

      <path class="accent-sweep" d="M172 1304 Q330 990 636 840 L636 1304 Z"/>

      <g class="brand">
        <rect class="brand-square" x="172" y="540" width="36" height="36"/>
        <text class="brand-name" x="226" y="574" textLength="370" lengthAdjust="spacingAndGlyphs">Korvo Supplies</text>
      </g>

      <g class="material-list">
        <g class="material-item">
          <rect class="material-tile" x="537" y="658" width="70" height="70" rx="8"/>
          <rect role="img" aria-label="Softwood timber sample" x="541" y="662" width="62" height="50" fill="var(--timber-light)"/>
          <rect class="material-band" x="537" y="713" width="70" height="15" rx="4"/>
          <text class="material-label" x="572" y="724" text-anchor="middle">WOOD</text>
        </g>
        <g class="material-item">
          <rect class="material-tile" x="537" y="740" width="70" height="70" rx="8"/>
          <rect role="img" aria-label="Hardwood plank sample" x="541" y="744" width="62" height="50" fill="var(--hardwood)"/>
          <rect class="material-band" x="537" y="795" width="70" height="15" rx="4"/>
          <text class="material-label" x="572" y="806" text-anchor="middle">HARDWOOD</text>
        </g>
        <g class="material-item">
          <rect class="material-tile" x="535" y="822" width="70" height="70" rx="8"/>
          <rect role="img" aria-label="Plywood sheet sample" x="539" y="826" width="62" height="50" fill="var(--plywood-top)"/>
          <rect class="material-band" x="535" y="877" width="70" height="15" rx="4"/>
          <text class="material-label" x="570" y="888" text-anchor="middle">PLYWOOD</text>
        </g>
      </g>

      <path class="product-window"
            d="M312 990 L312 835 A74.5 75 0 0 1 461 835 L461 990 L444 1013 L444 1140 L484 1180 L484 1190 Q484 1212 462 1212 L310 1212 Q288 1212 288 1190 L288 1180 L329 1140 L329 1013 Z"/>
    </g>
  </defs>

  <rect class="backdrop-light" x="0" y="0" width="750" height="1500"/>
  <rect class="backdrop-blue" x="750" y="0" width="750" height="1500"/>

  <use href="#blade-pack"/>
  <use href="#blade-pack" x="750"/>
</svg>
</body>
</html>
```